Brightwell Mechanical - Business Card Design

We would like a dark (likely black) themed business card to be able to hand out to potential clients. We may list our services on the card or keep it clean. Unsure. Logo attached

```html
<!DOCTYPE html>
<html lang="en">
<head>
<meta charset="utf-8">
<title>Brightwell Mechanical – Business Card</title>
<link href="https://fonts.googleapis.com/css2?family=Roboto:wght@400;500&display=swap" rel="stylesheet">
<style>
  :root {
    --stage: #cdd2d2;
    --card: #111111;
    --card-edge: #1f3fb8;
    --orange: #e2502a;
    --blue: #2553c9;
    --emboss: #3b3b3b;
  }
  * { box-sizing: border-box; margin: 0; padding: 0; }
  html, body { width: 1200px; height: 1200px; overflow: hidden; }
  body {
    background: var(--stage);
    font-family: "Roboto", Arial, sans-serif;
    display: flex;
    flex-direction: column;
    align-items: center;
    justify-content: center;
    gap: 56px;
  }
  .card {
    width: 900px;
    height: 514px;
    background: var(--card);
    border-bottom: 6px solid var(--card-edge);
    position: relative;
  }
  .card-front {
    display: grid;
    grid-template-columns: 1fr 2px 1fr;
    align-items: center;
    padding: 0 56px;
  }
  .brand {
    display: flex;
    align-items: center;
    gap: 16px;
    justify-content: center;
  }
  .brand-dot {
    width: 40px; height: 40px;
    border-radius: 50%;
    background: var(--orange);
    flex: none;
  }
  .brand-name {
    font-weight: 500;
    font-size: 30px;
    line-height: 1.15;
    color: var(--blue);
    text-transform: uppercase;
    letter-spacing: 1px;
  }
  .divider {
    width: 2px;
    height: 300px;
    background: var(--blue);
  }
  .contact { padding-left: 44px; }
  .person-name {
    color: var(--orange);
    font-size: 34px;
    font-weight: 400;
    text-transform: uppercase;
    letter-spacing: 0.5px;
  }
  .person-role {
    color: var(--blue);
    font-size: 22px;
    margin-bottom: 22px;
  }
  .address {
    color: var(--blue);
    font-size: 22px;
    line-height: 1.25;
    margin-bottom: 22px;
  }
  .contact-list { list-style: none; }
  .contact-list li {
    display: flex;
    align-items: center;
    gap: 14px;
    color: var(--blue);
    font-size: 22px;
    line-height: 1.45;
  }
  .contact-list svg { width: 18px; height: 18px; flex: none; }
  .card-back {
    display: flex;
    align-items: center;
    justify-content: center;
    gap: 20px;
  }
  .card-back .brand-dot { background: var(--emboss); width: 56px; height: 56px; }
  .card-back .brand-name { color: var(--emboss); font-size: 44px; }
</style>
</head>
<body>
  <section class="card card-front" aria-label="Business card front">
    <div class="brand">
      <span class="brand-dot"></span>
      <span class="brand-name">Brightwell<br>Mechanical</span>
    </div>
    <div class="divider"></div>
    <div class="contact">
      <h1 class="person-name">Daniel Harper</h1>
      <p class="person-role">Manager</p>
      <p class="address">Your address, city<br>state, ZIP 0000</p>
      <ul class="contact-list">
        <li>
          <svg viewBox="0 0 24 24" fill="var(--orange)" aria-hidden="true"><path d="M6.6 10.8a15.1 15.1 0 0 0 6.6 6.6l2.2-2.2a1 1 0 0 1 1-.25 11.4 11.4 0 0 0 3.6.57 1 1 0 0 1 1 1V20a1 1 0 0 1-1 1A17 17 0 0 1 3 4a1 1 0 0 1 1-1h3.5a1 1 0 0 1 1 1c0 1.25.2 2.45.57 3.57a1 1 0 0 1-.25 1z"/></svg>
          555-014-2100
        </li>
        <li>
          <svg viewBox="0 0 24 24" fill="none" stroke="var(--orange)" stroke-width="2" aria-hidden="true"><rect x="3" y="5" width="18" height="14" rx="1"/><path d="M3 6l9 7 9-7"/></svg>
          hello@brightwellmech.com
        </li>
        <li>
          <svg viewBox="0 0 24 24" fill="none" stroke="var(--orange)" stroke-width="2" aria-hidden="true"><circle cx="12" cy="12" r="9"/><path d="M3 12h18M12 3c3 3 3 15 0 18M12 3c-3 3-3 15 0 18"/></svg>
          www.brightwellmech.com
        </li>
      </ul>
    </div>
  </section>

  <section class="card card-back" aria-label="Business card back">
    <span class="brand-dot"></span>
    <span class="brand-name">Brightwell<br>Mechanical</span>
  </section>
</body>
</html>
```